Jewelers Website

This is for the DESIGN ONLY.
I am a software programmer and will be doing the development.
New website design for
www.lunagemcraft.com.au
Need a fresh new look for an online only jewellery business who produce their jewellery by hand. I would like it designed in a parallax style. Feel free to recommend fonts to use for the site. This is an Australian based company located in NSW so shots of sites in NSW might make nice background images.
http://plaxorin.me/demo/#theme=parallax
To contain the below sections
About Us
Contact Us
Gallery
Testimonials
Diamond Types
The colour scheme is to be Black / White and Silver.
With the Parallax style there will be moving sections and images for added impact.
Target Market(s)
Young Adults mainly engagement jewellery

```html
<!DOCTYPE html>
<html lang="en">
<head>
<meta charset="utf-8">
<title>Luna Gemcraft</title>
<link href="https://fonts.googleapis.com/css2?family=Ubuntu:wght@400;500;700&display=swap" rel="stylesheet">
<style>
:root{
  --ink:#1d1d1d;
  --header:#262626;
  --dark:#232323;
  --darker:#171717;
  --white:#ffffff;
  --grey-text:#555555;
  --footer:#6e6e6e;
  --footer-bottom:#3e3e3e;
  --silver:#c9c9c9;
  --hero-a:#c8dfee;
  --hero-b:#9fc2da;
  --caption:#5d7385;
}
*{box-sizing:border-box;margin:0;padding:0}
html,body{width:766px;height:1200px;overflow:hidden}
body{font-family:'Ubuntu',sans-serif;color:var(--ink);background:var(--white);position:relative}
.site-header{position:absolute;left:0;top:0;width:766px;height:58px;background:linear-gradient(90deg,#1f1f1f,#333 50%,#1f1f1f)}
.brand{position:absolute;left:113px;top:13px;color:var(--white);font-size:15px;line-height:15px;font-weight:400;letter-spacing:.5px;text-transform:uppercase}
.account-links{position:absolute;right:194px;top:10px;font-size:6.5px;color:#ccc}
.account-links span{margin:0 3px}
.social-top{position:absolute;left:579px;top:6px;display:flex;gap:5px}
.social-top i{display:block;width:15px;height:15px;border-radius:50%}
.search{position:absolute;left:531px;top:30px;width:120px;height:15px;display:flex;font-size:6.5px}
.search-field{flex:1;background:var(--white);color:#aaa;padding:4px 6px;border-radius:2px 0 0 2px}
.search-btn{width:38px;background:#e9e9e9;color:#111;font-weight:700;text-align:center;padding-top:4px;border-radius:0 2px 2px 0}
.main-nav{position:absolute;left:0;top:58px;width:766px;height:19px;background:linear-gradient(#fff,#e8e8e8);border-bottom:1px solid #cfcfcf;display:flex;padding-left:113px;align-items:center}
.main-nav a{font-size:7.5px;font-weight:700;color:var(--ink);text-decoration:none;padding:0 7px;border-left:1px solid #bbb;line-height:9px}
.main-nav a:first-child{padding-left:0;border-left:none}
.hero{position:absolute;left:0;top:77px;width:766px;height:239px;background:linear-gradient(180deg,var(--hero-a),var(--hero-b))}
.hero-photo{position:absolute;left:95px;top:10px;width:350px;height:225px;border-radius:50%;background:radial-gradient(circle at 50% 45%,#f4f6f8,#b9c9d6 55%,rgba(159,194,218,0) 72%)}
.hero-caption{position:absolute;left:478px;top:85px;width:174px;height:60px;background:var(--caption);opacity:.92;border:1px solid #c7d4de;color:var(--white);font-size:13px;font-weight:500;text-align:center;line-height:20px;padding-top:10px}
.hero-arrows{position:absolute;left:478px;top:163px}
.collection{position:absolute;left:0;top:316px;width:766px;height:255px;background:var(--white)}
.section-title{font-size:15px;font-weight:500;text-align:center}
.collection .section-title{margin-top:21px}
.features{position:absolute;left:113px;top:55px;width:539px;display:flex;justify-content:space-between}
.feature{width:168px;text-align:center}
.feature-photo{display:block;width:71px;height:71px;border-radius:50%;margin:0 auto}
.feature h3{font-size:11px;font-weight:500;margin-top:14px}
.feature p{font-size:6.6px;line-height:12.2px;color:var(--grey-text);margin-top:6px}
.btn{display:inline-block;margin-top:8px;background:var(--ink);color:var(--white);font-size:7px;font-weight:700;padding:5px 10px;border-radius:10px;border:1px solid #555}
.stories{position:absolute;left:0;top:571px;width:766px;height:225px;background:var(--dark);color:var(--white)}
.stories .section-title{margin-top:25px}
.story{position:absolute;top:61px;width:263px;height:112px;background:linear-gradient(90deg,#bdbdbd,#f6f6f6);color:var(--ink)}
.story::after{content:"";position:absolute;left:8px;bottom:-9px;border-left:0 solid transparent;border-right:10px solid transparent;border-top:9px solid #bdbdbd}
.story-photo{position:absolute;left:9px;top:21px;width:70px;height:70px;border-radius:50%;background:linear-gradient(135deg,#6f7a70,#c9c9c9)}
.story-body{position:absolute;left:92px;top:17px;width:160px;font-size:6.6px;line-height:12.2px}
.story-body h4{font-size:7.5px;font-weight:700}
.story-body .by{margin-top:5px}
.dots{position:absolute;left:0;width:766px;display:flex;justify-content:center;gap:4px}
.dots i{width:7px;height:7px;border-radius:50%;background:#bbb}
.dots i:first-child{background:#888}
.types{position:absolute;left:0;top:796px;width:766px;height:186px;background:var(--darker);color:var(--white)}
.types .section-title{margin-top:21px}
.type-list{position:absolute;left:111px;top:64px;width:543px;display:flex;justify-content:space-between}
.type{width:58px;text-align:center}
.type-gem{display:block;width:52px;height:52px;border-radius:50%;margin:0 auto;background:radial-gradient(circle,#f2f2f2 0,#b7b7b7 34%,#2b2b2b 46%,#111 72%);border:1px solid #444}
.type span{display:block;font-size:9px;color:#ccc;margin-top:13px}
.partners{position:absolute;left:0;top:982px;width:766px;height:71px;background:var(--white);display:flex;justify-content:center;align-items:center;gap:62px;color:#8c8c8c;font-size:15px;letter-spacing:1px}
.site-footer{position:absolute;left:0;top:1053px;width:766px;height:107px;background:var(--footer);color:#eee;font-size:6.5px}
.f-col{position:absolute;top:11px}
.f-col h5{font-size:7.5px;font-weight:700;margin-bottom:6px;text-transform:uppercase}
.f-col li{list-style:none;line-height:12.8px}
.f-col b{font-weight:700}
.signup-field{width:129px;height:20px;background:var(--white);border-radius:2px;color:#999;padding:6px 8px}
.signup-btn{display:inline-block;margin-top:7px;background:#111;color:var(--white);font-weight:700;padding:5px 11px;border-radius:2px;font-size:7px}
.follow li{display:flex;align-items:center;gap:8px;line-height:12px;margin-bottom:7px}
.follow i{display:block;width:19px;height:19px;border-radius:50%;background:var(--white)}
.footer-bottom{position:absolute;left:0;top:1160px;width:766px;height:40px;background:var(--footer-bottom);color:#ccc;font-size:6px;text-align:center;padding-top:10px;line-height:12px}
.footer-bottom span{margin:0 4px}
</style>
</head>
<body>
<header class="site-header">
  <div class="brand">Luna<br>Gemcraft</div>
  <div class="account-links">Register<span>|</span>Sign in<span>|</span>My Account</div>
  <div class="social-top"><i style="background:#cc2127"></i><i style="background:#2aa3ef"></i><i style="background:#3b5b9a"></i><i style="background:#f26522"></i></div>
  <div class="search"><div class="search-field">Search</div><div class="search-btn">SEARCH</div></div>
</header>
<nav class="main-nav">
  <a href="#">HOME</a><a href="#">ABOUT US</a><a href="#">CONTACT US</a><a href="#">GALLERY</a><a href="#">TESTIMONIALS</a><a href="#">DIAMOND TYPES</a>
</nav>
<section class="hero">
  <div class="hero-photo" role="img" aria-label="Close-up photograph of a diamond halo engagement ring on a pale blue surface"></div>
  <div class="hero-caption">THE WORLD’S MOST<br>BEAUTIFUL DIAMOND</div>
  <svg class="hero-arrows" width="30" height="14" viewBox="0 0 30 14"><path d="M7 1 1 7l6 6M17 1l6 6-6 6" fill="none" stroke="#333" stroke-width="1.2"/></svg>
</section>
<section class="collection">
  <h2 class="section-title">Diamond Engagement Rings &amp; Jewellery</h2>
  <div class="features">
    <div class="feature">
      <span class="feature-photo" role="img" aria-label="Photograph of loose diamonds" style="background:radial-gradient(circle,#f3f5f8,#bfcbe0)"></span>
      <h3>Diamond Jewelry</h3>
      <p>Lorem Ipsum is simply dummy text of the printing and typesetting industry. Lorem Ipsum has been the industry's standard dummy text ever since the 1500s, when an unknown.</p>
      <span class="btn">Learn More</span>
    </div>
    <div class="feature">
      <span class="feature-photo" role="img" aria-label="Photograph of gemstone drop earrings" style="background:radial-gradient(circle,#a9c6ee,#3d6fb8)"></span>
      <h3>Jewelry</h3>
      <p>Lorem Ipsum is simply dummy text of the printing and typesetting industry. Lorem Ipsum has been the industry's standard dummy text ever since the 1500s, when an unknown.</p>
      <span class="btn">Learn More</span>
    </div>
    <div class="feature">
      <span class="feature-photo" role="img" aria-label="Photograph of a diamond engagement ring" style="background:radial-gradient(circle,#e0eef5,#7fb0c6)"></span>
      <h3>Engagement Rings</h3>
      <p>Lorem Ipsum is simply dummy text of the printing and typesetting industry. Lorem Ipsum has been the industry's standard dummy text ever since the 1500s, when an unknown.</p>
      <span class="btn">Learn More</span>
    </div>
  </div>
</section>
<section class="stories">
  <h2 class="section-title">Stories &amp; Testimonials</h2>
  <article class="story" style="left:113px">
    <div class="story-photo" role="img" aria-label="Wedding photograph of a couple beside a vintage car"></div>
    <div class="story-body">
      <h4>Liam &amp; Sofia</h4>
      <p>Lorem Ipsum is simply dummy text of the printing and typesetting industry. Lorem Ipsum has been the industry's standard dummy text ever since the 1500s</p>
      <p class="by">Marion, Harlow, OR</p>
    </div>
  </article>
  <article class="story" style="left:389px">
    <div class="story-photo" role="img" aria-label="Wedding photograph of a couple in a white car" style="background:linear-gradient(135deg,#4a5a6e,#dcdcdc)"></div>
    <div class="story-body">
      <h4>Nico &amp; Elena</h4>
      <p>Lorem Ipsum is simply dummy text of the printing and typesetting industry. Lorem Ipsum has been the industry's standard dummy text ever since the 1500s</p>
      <p class="by">Marion, Harlow, OR</p>
    </div>
  </article>
  <div class="dots" style="top:194px"><i></i><i></i><i></i></div>
</section>
<section class="types">
  <h2 class="section-title">Diamond Types</h2>
  <div class="type-list">
    <div class="type"><span class="type-gem" role="img" aria-label="Round cut diamond"></span><span>Round</span></div>
    <div class="type"><span class="type-gem" role="img" aria-label="Princess cut diamond"></span><span>Princess</span></div>
    <div class="type"><span class="type-gem" role="img" aria-label="Cushion cut diamond"></span><span>Cushion</span></div>
    <div class="type"><span class="type-gem" role="img" aria-label="Asscher cut diamond"></span><span>Asscher</span></div>
    <div class="type"><span class="type-gem" role="img" aria-label="Asscher cut diamond"></span><span>Asscher</span></div>
    <div class="type"><span class="type-gem" role="img" aria-label="Heart cut diamond"></span><span>Heart</span></div>
    <div class="type"><span class="type-gem" role="img" aria-label="Oval cut diamond"></span><span>Oval</span></div>
    <div class="type"><span class="type-gem" role="img" aria-label="Emerald cut diamond"></span><span>Emarld</span></div>
  </div>
  <div class="dots" style="top:168px"><i></i><i></i><i></i></div>
</section>
<section class="partners">
  <span>NORVEL</span><span>AURELANE</span><span>KESTRA VALE</span><span>ORLANI</span>
</section>
<footer class="site-footer">
  <div class="f-col" style="left:113px"><h5>About Us</h5><ul><li>Careers</li><li>Quality &amp; Value</li><li>Investor Relations</li><li>In the News</li><li>Diamonds</li></ul></div>
  <div class="f-col" style="left:231px;top:24px"><ul><li>Gallery</li><li>Testimonials</li><li>Diamond Types</li><li>Locations</li><li>Legals</li></ul></div>
  <div class="f-col" style="left:331px"><h5>Contact</h5><ul><li><b>Sydney</b></li><li>Brindle NSW 2299, Australia</li><li>Phone +61 (0)2 5550 1234</li><li><b>Germany</b></li><li>40000 Feldhain, Germany</li><li>Phone +49 (0)2100 5550123</li></ul></div>
  <div class="f-col" style="left:448px"><h5>Sign Up For Special</h5><div class="signup-field">Your Email Address</div><span class="signup-btn">SIGN UP</span></div>
  <div class="f-col follow" style="left:599px"><h5 style="text-transform:none">Follow Us</h5><ul><li><i></i>Pagebook</li><li><i></i>Chirper</li><li><i></i>ViewTube</li></ul></div>
</footer>
<div class="footer-bottom">
  <div>Contact Us<span>|</span>Privacy &amp; Security<span>|</span>Terms of Use<span>|</span>Sitemap</div>
  <div>© t 2002-2012 Luna Gemcraft Pty Ltd (ABN 00 000 000 000). Luna Gemcraft also trades as</div>
</div>
</body>
</html>
```